M&A Advisory firm needs elegant and powerful letterhead

We need a powerful but elegant letterhead to engage with the international financial industry.

Target Market(s)

New York and International Financial Industry

Industry/Entity Type

Finance

Font styles to use
Other font styles liked:
• Poppins

Requirements
Must have
• 482 W 71st Street 14th Floor New York, NY 10157 O: +1 (212) 555 0147 F: +1 (212) 555 0182

```html
<!DOCTYPE html>
<html lang="en">
<head>
<meta charset="UTF-8">
<title>Meridane Letterhead</title>
<link href="https://fonts.googleapis.com/css2?family=Open+Sans:wght@400;600&display=swap" rel="stylesheet">
<style>
  :root {
    --backdrop-light: #dcdedd;
    --backdrop-dark: #b7b9ba;
    --paper: #ffffff;
    --brand-blue: #0d5699;
    --accent-gray: #7d7e80;
    --tagline-gray: #8a8b8d;
    --ink: #1c1c1c;
  }
  * { margin: 0; padding: 0; box-sizing: border-box; }
  html, body { width: 1200px; height: 686px; overflow: hidden; }
  body {
    background: linear-gradient(180deg, var(--backdrop-light), var(--backdrop-dark));
    font-family: "Open Sans", Arial, sans-serif;
    position: relative;
  }
  .letterhead {
    position: absolute;
    left: 352px;
    top: 22px;
    width: 496px;
    height: 642px;
    background: var(--paper);
    box-shadow: 0 6px 18px rgba(0,0,0,0.18);
    overflow: hidden;
  }
  .brand {
    position: absolute;
    left: 40px;
    top: 36px;
    display: flex;
    align-items: center;
    gap: 10px;
  }
  .brand-dot {
    width: 22px;
    height: 22px;
    border-radius: 50%;
    background: var(--brand-blue);
  }
  .brand-name {
    font-size: 30px;
    font-weight: 400;
    letter-spacing: 1px;
    color: var(--brand-blue);
    line-height: 1;
  }
  .brand-tagline {
    position: absolute;
    left: 72px;
    top: 72px;
    font-size: 7px;
    letter-spacing: 2.4px;
    color: var(--tagline-gray);
    white-space: nowrap;
  }
  .footer-bands {
    position: absolute;
    left: 0;
    bottom: 0;
    width: 496px;
    height: 60px;
  }
  .contact {
    position: absolute;
    right: 22px;
    bottom: 46px;
    text-align: right;
    font-size: 11px;
    line-height: 1.3;
    color: var(--ink);
  }
  .contact-line {
    display: flex;
    justify-content: flex-end;
    align-items: center;
    gap: 8px;
  }
  .contact-group + .contact-group { margin-top: 10px; }
  .contact-icon { width: 10px; height: 10px; flex: none; }
</style>
</head>
<body>
  <main class="letterhead">
    <div class="brand">
      <span class="brand-dot"></span>
      <span class="brand-name">MERIDANE</span>
    </div>
    <p class="brand-tagline">Clarity in Every Deal</p>

    <div class="contact">
      <div class="contact-group">
        <div class="contact-line"><span>482 W 71st Street 14th Floor</span><span class="contact-icon"></span></div>
        <div class="contact-line"><span>New York, NY 10157</span>
          <svg class="contact-icon" viewBox="0 0 10 10"><path d="M5 0.5a3 3 0 0 1 3 3c0 2.2-3 5.8-3 5.8S2 5.7 2 3.5a3 3 0 0 1 3-3z" fill="var(--brand-blue)"/><circle cx="5" cy="3.5" r="1.1" fill="#fff"/></svg>
        </div>
      </div>
      <div class="contact-group">
        <div class="contact-line"><span>+1 (212) 555 0147</span>
          <svg class="contact-icon" viewBox="0 0 10 10"><path d="M2.2 0.8l1.6 1.8-0.9 1.3c0.5 1.2 1.6 2.3 2.8 2.8l1.3-0.9 1.8 1.6-1 1.4C4.6 8.6 1.4 5.4 0.8 1.8z" fill="var(--brand-blue)"/></svg>
        </div>
        <div class="contact-line"><span>+1 (212) 555 0182</span>
          <svg class="contact-icon" viewBox="0 0 10 10"><rect x="0.5" y="3" width="9" height="6.5" rx="1" fill="var(--brand-blue)"/><rect x="2.5" y="0.5" width="5" height="3" fill="var(--brand-blue)"/><rect x="2.5" y="5" width="5" height="2.5" fill="#fff"/></svg>
        </div>
      </div>
    </div>

    <svg class="footer-bands" viewBox="0 0 496 60" aria-hidden="true">
      <path d="M0 40 H280 Q291 40 298 47" fill="none" stroke="var(--accent-gray)" stroke-width="3"/>
      <path d="M0 50 H290 Q302 50 312 42 Q320 36 332 36 H496 V60 H0 Z" fill="var(--brand-blue)"/>
    </svg>
  </main>
</body>
</html>
```